Wordpress Contest Brief I would like a WordPress theme designed

Industry / Entity Type

Financial consultancy / advisers

Current site is: http://www.quorvel-group.com

Looking for a complete overhaul of this site, we are after a clean modern look. Will require the ability to easily add, update and remove content, hence the WordPress design.
Example:
Add case studies
Industry documentation (downloadable brochures / flyers and such)

What we like from our current site is the colour the fonts and the logo (the city of London) we would like to have other city outlines (NYC and Tokyo, Hong Kong, Singapore).

The site will be used by our potential clients to get in contact and re-view the case studies, if possible would like to have a client login area where they can download our documents like NDA’s etc and T&C’s.

Task Outline

Create a Web Design (Coded - Design and coding required)
Designer must provide full implementation/coding depending on the platform chosen by the client (i.e. WordPress theme, HTML/CSS, bootstrap etc.)

Task Description

I need a full website built that must work on desktop and mobile. I can provide the London city skyline and the font file, which we have used. Some stock industrial photos will be required.

Requirements:

*Splash page
*What We Do
*How We do it
*Who Are We? To have the same information and links as the current site
*Why use us?
*Clients: To have the same information and links as the current site
*Partners: To have the same information and links as the current site
*Contact:

Target Market(s)

Financial institutions trading Equities, Futures, Options, Forex and Fixed Income.
Regulators, Exchanges, ECN’s
Buy side firms and Sell side firms

Industry/Entity Type

Financial

Coding

Coded - Design and coding required

Number of Pages Required

5+ page

Font styles to use
Sans Serif

Colors
f04a50

Requirements
Must have
• Splash page
• What We Do
• How We do it
• Who Are We? To have the same information and links as the current site
• Why use us?
• Clients: To have the same information and links as the current site
• Partners: To have the same information and links as the current site
• Contact:

```html
<!DOCTYPE html>
<html lang="en">
<head>
<meta charset="utf-8">
<title>Quorvel Group</title>
<link rel="stylesheet" href="https://fonts.googleapis.com/css2?family=Open+Sans:wght@400;600&display=swap">
<style>
  :root {
    --brand-red: #f04a50;
    --hero-line: #f46a6f;
    --nav-dark: #2a2b30;
    --panel-dark: #3b2b30;
    --panel-edge: #2e2428;
    --text-light: #ffffff;
    --text-soft: #e8e2e3;
  }
  * { box-sizing: border-box; margin: 0; padding: 0; }
  html, body {
    width: 1200px; height: 762px; overflow: hidden;
    background: #ffffff;
    font-family: "Open Sans", Arial, sans-serif;
  }
  .site {
    position: relative; width: 1200px; height: 762px;
    background: var(--brand-red);
    color: var(--text-light);
  }
  a { color: inherit; text-decoration: none; }
  ul { list-style: none; }

  /* Top navigation */
  .top-strip { height: 11px; background: var(--brand-red); }
  .main-nav {
    position: relative; height: 64px; background: var(--nav-dark);
  }
  .main-nav__link {
    position: absolute; top: 17px; font-size: 21px; letter-spacing: 0.3px;
    color: var(--text-soft);
  }
  .social-square {
    position: absolute; top: 23px; width: 18px; height: 18px;
    background: var(--text-light); border-radius: 2px;
  }
  .search-icon { position: absolute; top: 20px; left: 1023px; }
  .menu-toggle { position: absolute; top: 19px; left: 1129px; }

  /* Hero */
  .hero { position: relative; height: 473px; }
  .skyline {
    position: absolute; left: 335px; top: 135px; width: 510px; height: 166px;
    background: linear-gradient(180deg, rgba(255,255,255,0) 0%, rgba(255,255,255,0.18) 100%);
    border-bottom: 2px solid rgba(255,255,255,0.7);
  }
  .hero__name {
    position: absolute; left: 0; right: 0; top: 318px;
    text-align: center; font-size: 44px; font-weight: 600;
    letter-spacing: 10px; color: var(--text-light);
  }

  /* Dropdown panel */
  .sub-menu {
    position: absolute; left: 917px; top: 81px; width: 282px; height: 280px;
    background: var(--panel-dark);
    border-top: 15px solid var(--panel-edge);
    border-bottom: 7px solid var(--panel-edge);
    padding: 20px 0 0 38px;
  }
  .sub-menu li { font-size: 19px; line-height: 39px; color: var(--text-soft); }

  /* Footer */
  .footer-band { height: 17px; background: var(--nav-dark); }
  .site-footer { position: relative; height: 167px; background: var(--panel-dark); }
  .footer-links { position: absolute; top: 12px; }
  .footer-links li { font-size: 20px; line-height: 36.5px; color: var(--text-soft); }
  .footer-links--main { left: 103px; }
  .footer-links--sections { left: 368px; top: 13px; }
  .contact-list { position: absolute; left: 806px; top: 4px; }
  .contact-item {
    position: relative; padding-left: 34px;
    font-size: 21px; font-weight: 600; line-height: 26px; color: var(--text-light);
  }
  .contact-item svg { position: absolute; left: 0; }
  .contact-item--phone { height: 38px; }
  .contact-item--phone svg { top: 4px; }
  .contact-item--email { height: 38px; padding-left: 40px; }
  .contact-item--email svg { top: 7px; }
  .contact-item--address svg { top: 28px; left: 4px; }
  .copyright {
    height: 30px; background: var(--nav-dark);
    text-align: center; font-size: 14px; line-height: 30px; color: var(--text-soft);
  }
</style>
</head>
<body>
<div class="site">
  <div class="top-strip"></div>
  <nav class="main-nav" aria-label="Main">
    <a class="main-nav__link" style="left:103px" href="#">HOME</a>
    <a class="main-nav__link" style="left:309px" href="#">CLIENTS</a>
    <a class="main-nav__link" style="left:512px" href="#">PARTNERS</a>
    <a class="main-nav__link" style="left:716px" href="#">CONTACT</a>
    <span class="social-square" style="left:922px" aria-label="Social profile"></span>
    <span class="social-square" style="left:973px" aria-label="Social profile"></span>
    <svg class="search-icon" width="22" height="22" viewBox="0 0 22 22" aria-label="Search">
      <circle cx="9" cy="9" r="6.5" fill="none" stroke="#fff" stroke-width="3"/>
      <line x1="14" y1="14" x2="20" y2="20" stroke="#fff" stroke-width="3.5" stroke-linecap="round"/>
    </svg>
    <svg class="menu-toggle" width="40" height="28" viewBox="0 0 40 28" aria-label="Menu">
      <rect x="0" y="0" width="40" height="4" fill="#fff"/>
      <rect x="0" y="12" width="40" height="4" fill="#fff"/>
      <rect x="0" y="24" width="28" height="4" fill="#fff"/>
    </svg>
  </nav>

  <section class="hero">
    <div class="skyline" role="img" aria-label="Line drawing of the London city skyline"></div>
    <h1 class="hero__name">QUORVEL GROUP</h1>
  </section>

  <ul class="sub-menu">
    <li>WHAT WE DO</li>
    <li>HOW WE DO IT</li>
    <li>WHO ARE WE?</li>
    <li>WHY USE US?</li>
  </ul>

  <div class="footer-band"></div>
  <footer class="site-footer">
    <ul class="footer-links footer-links--main">
      <li>HOME</li><li>CLIENTS</li><li>PARTNERS</li><li>CONTACT</li>
    </ul>
    <ul class="footer-links footer-links--sections">
      <li>WHAT WE DO</li><li>HOW WE DO IT</li><li>WHO ARE WE?</li><li>WHY USE US?</li>
    </ul>
    <ul class="contact-list">
      <li class="contact-item contact-item--phone">
        <svg width="20" height="20" viewBox="0 0 20 20" aria-hidden="true">
          <path d="M4 1 L7.5 1 L9 6 L6.5 7.8 C7.6 10.2 9.8 12.4 12.2 13.5 L14 11 L19 12.5 L19 16 C19 17.8 17.8 19 16 19 C8 19 1 12 1 4 C1 2.2 2.2 1 4 1 Z" fill="#fff"/>
        </svg>
        +44(0)20 7946 0831
      </li>
      <li class="contact-item contact-item--email">
        <svg width="24" height="17" viewBox="0 0 24 17" aria-hidden="true">
          <rect x="0" y="0" width="24" height="17" rx="1.5" fill="#fff"/>
          <path d="M1 1.5 L12 9.5 L23 1.5" fill="none" stroke="#3b2b30" stroke-width="2"/>
        </svg>
        admin@quorvel-group.com
      </li>
      <li class="contact-item contact-item--address">
        <svg width="14" height="20" viewBox="0 0 14 20" aria-hidden="true">
          <path d="M7 0 C3.1 0 0 3.1 0 7 C0 12 7 20 7 20 C7 20 14 12 14 7 C14 3.1 10.9 0 7 0 Z" fill="#fff"/>
          <circle cx="7" cy="7" r="2.6" fill="#3b2b30"/>
        </svg>
        Suite 4 Harlow Court,<br>Brenfield, Hadley Cross,<br>Wessex, HC7 2LP
      </li>
    </ul>
  </footer>
  <div class="copyright">Copyright © 2017 Quorvel Group</div>
</div>
</body>
</html>
```